Social Action Network Needs Banner Ads for Cause T-Shirts

Lend a Hand is a social action network that transforms ordinary internet actions into donations to non-profit organizations fighting for a better tomorrow. Users can donate their social influence, print coupons, accept free offers or shop online and every action benefits causes they love. You can watch a video here: http://www.lendahandhub.example/

We are about to launch a line of cause tees that benefit the various causes we support. We want the banner ads to be positive, uplifting, inspiring and attractive. We want the ads to incorporate the following wording (although, we encourage creativity): Dress better so others can live better.

We require typical banner ad sizes: 300 x 250, 160 x 600, 728 x 90 (more sizes would be much appreciated).

Please try to include the Lend a Hand logo (color can be changed based on ad design).

In case it helps, here is a link to a page we have set up for one of our partner charities: http://www.lendahandhub.example/BrightWellFund

Target Market(s)

While 80% of our users are women, we need to appeal to both.

Industry/Entity Type

Non-Profit

Requirements
Must have
• Lend a Hand logo and T-shirt design (with or without model). Also, some sort of call to action button - get tees, take action, buy now, check it out, learn more, etc.
Nice to have
• Feature the woman's tees and if possible the man's tees could be somewhere smaller in the background (if design allows).

```html
<!DOCTYPE html>
<html lang="en">
<head>
<meta charset="utf-8">
<title>Lend a Hand – Cause Tee Banner Set</title>
<link rel="stylesheet" href="https://fonts.googleapis.com/css2?family=Special+Elite&family=Noto+Serif&family=Roboto+Condensed:wght@400;700&display=swap">
<style>
  :root {
    --board: #c9a67a;
    --sky: #1192e4;
    --sky-deep: #0670c4;
    --ribbon: #a80d0d;
    --tag-ink: #0c1e2b;
    --tag-text: #f4f4f4;
    --panel: #f2f2f2;
    --brand-ink: #1f1f1f;
    --brand-red: #b40f0f;
    --cta-top: #e42424;
    --cta-bottom: #a30000;
    --guide: rgba(112, 80, 48, 0.55);
    --guide-text: #f6ecdc;
    --footer: #1c1c1c;
  }
  * { box-sizing: border-box; margin: 0; padding: 0; }
  html, body { width: 1200px; height: 1094px; overflow: hidden; }
  body { background: var(--board); position: relative; font-family: "Noto Serif", serif; }

  .ad { position: absolute; background: var(--panel); overflow: hidden; box-shadow: 0 2px 6px rgba(0,0,0,.35); }
  .ad--wide { background: #fff; }
  .ad--tower { background: #fff; }
  .ad__sky { position: absolute; inset: 0; width: 100%; height: 100%; }
  .ad__art {
    position: absolute; border-radius: 46%;
    background: radial-gradient(ellipse at 55% 50%, #2f5f9c 0%, #2a6cb4 45%, rgba(17,146,228,0) 72%);
  }
  .tag {
    position: absolute; background: var(--tag-ink); color: var(--tag-text);
    font-family: "Special Elite", monospace; white-space: nowrap;
    padding: 2px 7px; line-height: 1.2; transform: rotate(-1.5deg);
  }
  .brand-dot { position: absolute; border-radius: 50%; background: var(--brand-ink); }
  .brand-name { position: absolute; color: var(--brand-ink); font-family: "Noto Serif", serif; white-space: nowrap; line-height: 1; }
  .brand-line {
    position: absolute; color: var(--brand-red); font-family: "Roboto Condensed", sans-serif;
    text-transform: uppercase; line-height: 1.15; text-align: center;
  }
  .cta {
    position: absolute; display: flex; align-items: center; justify-content: center;
    background: linear-gradient(var(--cta-top), var(--cta-bottom)); color: #fff;
    font-family: "Roboto Condensed", sans-serif; font-weight: 700; text-transform: uppercase;
    border-radius: 3px; box-shadow: 0 2px 3px rgba(0,0,0,.35);
  }

  .size-guide {
    position: absolute; background: var(--guide); color: var(--guide-text);
    font-family: "Noto Serif", serif; font-size: 16px; display: flex; align-items: center; justify-content: center;
    text-align: center; line-height: 1;
  }

  .footer { position: absolute; left: 0; top: 948px; width: 1200px; height: 146px; background: var(--footer); }
  .footer__dot { position: absolute; left: 93px; top: 18px; width: 106px; height: 106px; border-radius: 50%; border: 5px solid #fff; }
  .footer__name { position: absolute; left: 210px; top: 40px; color: #fff; font-size: 58px; line-height: 1; font-family: "Noto Serif", serif; }
  .footer__line { position: absolute; left: 292px; top: 98px; color: var(--brand-red); font-family: "Roboto Condensed", sans-serif; font-size: 15px; text-transform: uppercase; }
</style>
</head>
<body>

<!-- 250 x 250 -->
<section class="ad ad--square" style="left:134px;top:20px;width:250px;height:250px">
  <svg class="ad__sky" viewBox="0 0 250 250" preserveAspectRatio="none">
    <path d="M0,0H250V167Q130,152 0,151Z" fill="var(--ribbon)"/>
    <path d="M0,0H250V162Q130,147 0,146Z" fill="var(--sky)"/>
  </svg>
  <div class="ad__art" role="img" aria-label="Hand-lettered slogan 'Tomorrow can be Better' over a blue brush swirl" style="left:118px;top:12px;width:128px;height:132px"></div>
  <span class="tag" style="left:6px;top:40px;font-size:16px">Dress better</span>
  <span class="tag" style="left:8px;top:74px;font-size:13px">so others can</span>
  <span class="tag" style="left:8px;top:102px;font-size:18px">live better</span>
  <span class="brand-dot" style="left:46px;top:164px;width:40px;height:40px"></span>
  <span class="brand-name" style="left:10px;top:205px;font-size:18px">lend a hand</span>
  <span class="brand-line" style="left:6px;top:223px;width:120px;font-size:9px">where every action<br>has impact</span>
  <span class="cta" style="left:135px;top:192px;width:98px;height:30px;font-size:15px">Buy now</span>
</section>

<!-- 468 x 60 -->
<section class="ad ad--wide" style="left:414px;top:72px;width:468px;height:60px">
  <svg class="ad__sky" viewBox="0 0 468 60" preserveAspectRatio="none">
    <path d="M0,0H296Q285,30 292,60H0Z" fill="var(--ribbon)"/>
    <path d="M0,0H291Q280,30 287,60H0Z" fill="var(--sky)"/>
  </svg>
  <div class="ad__art" role="img" aria-label="Hand-lettered slogan 'Tomorrow can be Better' over a blue brush swirl" style="left:190px;top:2px;width:92px;height:56px"></div>
  <span class="tag" style="left:12px;top:11px;font-size:12px">Dress better so others</span>
  <span class="tag" style="left:38px;top:33px;font-size:12px">can live better</span>
  <span class="brand-dot" style="left:320px;top:6px;width:32px;height:32px"></span>
  <span class="brand-name" style="left:295px;top:41px;font-size:13px">lend a hand</span>
  <span class="cta" style="left:390px;top:19px;width:68px;height:25px;font-size:11px">Buy now</span>
</section>

<!-- 728 x 90 -->
<section class="ad ad--wide" style="left:414px;top:153px;width:728px;height:90px">
  <svg class="ad__sky" viewBox="0 0 728 90" preserveAspectRatio="none">
    <path d="M0,0H420Q404,45 412,90H0Z" fill="var(--ribbon)"/>
    <path d="M0,0H414Q398,45 405,90H0Z" fill="var(--sky)"/>
  </svg>
  <div class="ad__art" role="img" aria-label="Hand-lettered slogan 'Tomorrow can be Better' over a blue brush swirl" style="left:268px;top:2px;width:140px;height:86px"></div>
  <span class="tag" style="left:14px;top:15px;font-size:19px">Dress better so others</span>
  <span class="tag" style="left:50px;top:50px;font-size:19px">can live better</span>
  <span class="brand-dot" style="left:486px;top:5px;width:44px;height:44px"></span>
  <span class="brand-name" style="left:435px;top:50px;font-size:24px">lend a hand</span>
  <span class="brand-line" style="left:435px;top:72px;font-size:10px;text-align:left">where every action has impact</span>
  <span class="cta" style="left:607px;top:30px;width:98px;height:32px;font-size:15px">Buy now</span>
</section>

<!-- 300 x 250 -->
<section class="ad ad--square" style="left:85px;top:300px;width:300px;height:250px">
  <svg class="ad__sky" viewBox="0 0 300 250" preserveAspectRatio="none">
    <path d="M0,0H300V177Q150,154 0,148Z" fill="var(--ribbon)"/>
    <path d="M0,0H300V171Q150,148 0,142Z" fill="var(--sky)"/>
  </svg>
  <div class="ad__art" role="img" aria-label="Hand-lettered slogan 'Tomorrow can be Better' over a blue brush swirl" style="left:148px;top:14px;width:144px;height:150px"></div>
  <span class="tag" style="left:12px;top:28px;font-size:18px">Dress better</span>
  <span class="tag" style="left:16px;top:66px;font-size:15px">so others can</span>
  <span class="tag" style="left:12px;top:100px;font-size:20px">live better</span>
  <span class="brand-dot" style="left:54px;top:168px;width:44px;height:44px"></span>
  <span class="brand-name" style="left:12px;top:210px;font-size:22px">lend a hand</span>
  <span class="brand-line" style="left:12px;top:231px;font-size:10px;text-align:left">where every action has impact</span>
  <span class="cta" style="left:187px;top:198px;width:98px;height:32px;font-size:15px">Buy now</span>
</section>

<!-- 336 x 280 -->
<section class="ad ad--square" style="left:49px;top:581px;width:336px;height:280px">
  <svg class="ad__sky" viewBox="0 0 336 280" preserveAspectRatio="none">
    <path d="M0,0H336V188Q168,164 0,158Z" fill="var(--ribbon)"/>
    <path d="M0,0H336V182Q168,158 0,152Z" fill="var(--sky)"/>
  </svg>
  <div class="ad__art" role="img" aria-label="Hand-lettered slogan 'Tomorrow can be Better' over a blue brush swirl" style="left:166px;top:14px;width:162px;height:152px"></div>
  <span class="tag" style="left:20px;top:28px;font-size:19px">Dress better</span>
  <span class="tag" style="left:22px;top:72px;font-size:16px">so others can</span>
  <span class="tag" style="left:20px;top:106px;font-size:21px">live better</span>
  <span class="brand-dot" style="left:60px;top:186px;width:52px;height:52px"></span>
  <span class="brand-name" style="left:12px;top:238px;font-size:23px">lend a hand</span>
  <span class="brand-line" style="left:12px;top:259px;font-size:10px;text-align:left">where every action has impact</span>
  <span class="cta" style="left:191px;top:216px;width:112px;height:36px;font-size:16px">Buy now</span>
</section>

<!-- 160 x 600 -->
<section class="ad ad--tower" style="left:414px;top:262px;width:160px;height:600px">
  <svg class="ad__sky" viewBox="0 0 160 600" preserveAspectRatio="none">
    <path d="M0,0H160V412Q80,394 0,390Z" fill="var(--ribbon)"/>
    <path d="M0,0H160V406Q80,388 0,384Z" fill="var(--sky)"/>
  </svg>
  <div class="ad__art" role="img" aria-label="Hand-lettered slogan 'Tomorrow can be Better' over a blue brush swirl" style="left:8px;top:44px;width:148px;height:168px"></div>
  <span class="tag" style="left:8px;top:242px;font-size:18px">Dress better</span>
  <span class="tag" style="left:12px;top:288px;font-size:15px">so others can</span>
  <span class="tag" style="left:12px;top:330px;font-size:20px">live better</span>
  <span class="brand-dot" style="left:54px;top:428px;width:52px;height:52px"></span>
  <span class="brand-name" style="left:6px;top:478px;font-size:22px">lend a hand</span>
  <span class="brand-line" style="left:0;top:501px;width:160px;font-size:9px">where every action has impact</span>
  <span class="cta" style="left:29px;top:543px;width:98px;height:32px;font-size:15px">Buy now</span>
</section>

<!-- 120 x 600 -->
<section class="ad ad--tower" style="left:597px;top:264px;width:120px;height:600px">
  <svg class="ad__sky" viewBox="0 0 120 600" preserveAspectRatio="none">
    <path d="M0,0H120V392Q60,380 0,374Z" fill="var(--ribbon)"/>
    <path d="M0,0H120V386Q60,374 0,368Z" fill="var(--sky)"/>
  </svg>
  <div class="ad__art" role="img" aria-label="Hand-lettered slogan 'Tomorrow can be Better' over a blue brush swirl" style="left:2px;top:62px;width:116px;height:150px"></div>
  <span class="tag" style="left:6px;top:238px;font-size:14px">Dress better</span>
  <span class="tag" style="left:8px;top:273px;font-size:11px">so others can</span>
  <span class="tag" style="left:6px;top:302px;font-size:14px">live better</span>
  <span class="brand-dot" style="left:35px;top:410px;width:50px;height:50px"></span>
  <span class="brand-name" style="left:6px;top:462px;font-size:17px">lend a hand</span>
  <span class="brand-line" style="left:0;top:482px;width:120px;font-size:9px">where every action<br>has impact</span>
  <span class="cta" style="left:9px;top:540px;width:98px;height:32px;font-size:15px">Buy now</span>
</section>

<!-- Size guide -->
<div class="size-guide" style="left:790px;top:403px;width:96px;height:94px">250x250</div>
<div class="size-guide" style="left:897px;top:423px;width:179px;height:22px">468x60</div>
<div class="size-guide" style="left:897px;top:453px;width:278px;height:35px">728x90</div>
<div class="size-guide" style="left:772px;top:510px;width:114px;height:94px">300x250</div>
<div class="size-guide" style="left:758px;top:617px;width:128px;height:105px">336x280</div>
<div class="size-guide" style="left:897px;top:495px;width:61px;height:227px">160<br>x<br>600</div>
<div class="size-guide" style="left:967px;top:495px;width:46px;height:227px">120<br>x<br>600</div>

<!-- Brand footer -->
<footer class="footer">
  <span class="footer__dot"></span>
  <span class="footer__name">lend a hand</span>
  <span class="footer__line">where every action has impact</span>
</footer>

</body>
</html>
```